Need updated stationery design for chiropractic clinic

We recently moved our office and are looking to refresh our letterhead, business cards, presentation folder and envelopes. I tend to prefer simple, clean designs. We communicate with a lot of attorneys and want to exude professionalism. I have attached our logo and 2 additional versions (all white and white letters instead of grey).

Target Market(s)

Other medical professionals and attorneys. Business cards will go to patients as well.

Industry/Entity Type

Healthcare

```html
<!DOCTYPE html>
<html lang="en">
<head>
<meta charset="utf-8">
<title>Alignwell stationery</title>
<link href="https://fonts.googleapis.com/css2?family=Open+Sans:wght@400;700&display=swap" rel="stylesheet">
<style>
  :root {
    --brand-blue: #1a9bcf;
    --brand-teal: #3bc1c8;
    --soft-teal: #a8dde0;
    --soft-blue: #98c4e4;
    --paper: #ffffff;
    --frame: #222222;
  }
  * { margin: 0; padding: 0; box-sizing: border-box; }
  html, body {
    width: 1200px; height: 1000px; overflow: hidden;
    background: var(--paper);
    font-family: "Open Sans", Arial, sans-serif;
  }
  .canvas { position: relative; width: 1200px; height: 1000px; }

  /* Folder cover */
  .folder-cover {
    position: absolute; left: 70px; top: 28px; width: 519px; height: 734px;
    background: var(--brand-blue);
  }
  .folder-cover__name {
    position: absolute; left: 0; right: 0; top: 357px;
    text-align: center; color: var(--paper);
    font-weight: 700; font-size: 15px;
  }
  .folder-cover__band {
    position: absolute; left: 0; bottom: 0; width: 100%; height: 131px;
    background: var(--brand-teal);
  }
  .band-brand {
    position: absolute; left: 48px; top: 47px;
    color: var(--paper); font-weight: 700; font-size: 21px; line-height: 1;
    display: flex; align-items: center; gap: 8px;
  }
  .band-brand__square { width: 14px; height: 14px; background: var(--paper); }
  .contact-grid {
    position: absolute; left: 266px; top: 47px;
    display: grid; grid-template-columns: 101px 120px; row-gap: 8px;
    color: var(--paper); font-size: 6.5px;
  }
  .contact-item { display: flex; align-items: center; gap: 6px; white-space: nowrap; }
  .contact-item svg { width: 8px; height: 8px; flex: none; }

  /* Letterhead */
  .letterhead {
    position: absolute; left: 611px; top: 28px; width: 520px; height: 735px;
    background: var(--paper); border: 1px solid var(--frame);
  }
  .letterhead__decoration {
    position: absolute; left: 12px; top: 120px; width: 494px; height: 495px;
    background: linear-gradient(135deg, var(--soft-teal) 0%, var(--soft-blue) 50%, var(--soft-teal) 100%);
  }
  .letterhead__panel {
    position: absolute; left: 111px; top: 319px; width: 296px; height: 98px;
    background: var(--paper);
    display: flex; align-items: center; justify-content: center;
  }
  .letterhead__name {
    color: var(--brand-blue); font-weight: 700; font-size: 26px;
  }

  /* Envelope */
  .envelope {
    position: absolute; left: 70px; top: 783px; width: 519px; height: 188px;
    background: var(--brand-blue);
  }
  .envelope__name {
    position: absolute; left: 0; right: 0; top: 78px;
    text-align: center; color: var(--paper);
    font-weight: 700; font-size: 21px;
  }
</style>
</head>
<body>
<div class="canvas">

  <section class="folder-cover">
    <div class="folder-cover__name">Alignwell</div>
    <div class="folder-cover__band">
      <div class="band-brand"><span class="band-brand__square"></span>Alignwell</div>
      <div class="contact-grid">
        <div class="contact-item">
          <svg viewBox="0 0 10 10" fill="none" stroke="#fff" stroke-width="1.2"><path d="M2 1h2l1 2-1.2 1a5 5 0 0 0 2.2 2.2L7 5l2 1v2a1 1 0 0 1-1 1A7 7 0 0 1 1 2a1 1 0 0 1 1-1z"/></svg>
          <span>+014-555-0192</span>
        </div>
        <div class="contact-item">
          <svg viewBox="0 0 10 10" fill="none" stroke="#fff" stroke-width="1.1"><circle cx="5" cy="5" r="4"/><path d="M1 5h8M5 1c-2 2.5-2 5.5 0 8M5 1c2 2.5 2 5.5 0 8"/></svg>
          <span>alignwell.com</span>
        </div>
        <div class="contact-item">
          <svg viewBox="0 0 10 10" fill="none" stroke="#fff" stroke-width="1.1"><rect x="1" y="2" width="8" height="6"/><path d="M1 2l4 3.5L9 2"/></svg>
          <span>hello@alignwell.com</span>
        </div>
        <div class="contact-item">
          <svg viewBox="0 0 10 10" fill="none" stroke="#fff" stroke-width="1.1"><path d="M5 9.5S1.8 6 1.8 4a3.2 3.2 0 0 1 6.4 0C8.2 6 5 9.5 5 9.5z"/><circle cx="5" cy="4" r="1.1"/></svg>
          <span>48 Mill Lane, Easton, UK</span>
        </div>
      </div>
    </div>
  </section>

  <section class="letterhead">
    <div class="letterhead__decoration" role="img" aria-label="Large soft teal and blue brand decoration behind the name"></div>
    <div class="letterhead__panel">
      <div class="letterhead__name">Alignwell</div>
    </div>
  </section>

  <section class="envelope">
    <div class="envelope__name">Alignwell</div>
  </section>

</div>
</body>
</html>
```